New Label Design Project

DetailHi, we are a small Farm growing and selling fresh and dehydrated exotic vegetables to exotic market and ethnic restaurants. We plan to make changes our packaging by using clamshell instead of bags. This is why we send you this project. Our main Target Market are Jamaican, Haitian, Egyptian and Turkish restaurant. Small supermarket Markets like Zelto, Marcovina, Lunbrook Food Market, Quill food Market.... I sale to reseller in some farmers Market in Florida and Massachusetts. Then we have some direct customers they pick it at the farm stand. We don't have any online presence, my apologies... We are still working on that... We send you different logo. We are still working on the sizes of the clamshell. s for my new Label Design Project will be added soon.

```html
<!DOCTYPE html>
<html lang="en">
<head>
<meta charset="utf-8">
<title>Tallow Creek Farm – Clamshell Label</title>
<link rel="stylesheet" href="https://fonts.googleapis.com/css2?family=Bebas+Neue&family=Roboto+Slab:wght@400;500&display=swap">
<style>
  :root {
    --backdrop: #c0c0c0;
    --label-white: #ffffff;
    --ink: #111111;
    --leaf-green: #83a967;
    --brand-plum: #2d1a33;
  }
  html, body {
    margin: 0;
    width: 1200px;
    height: 850px;
    overflow: hidden;
    background: var(--backdrop);
  }
  .canvas {
    width: 1200px;
    height: 850px;
    display: flex;
    align-items: center;
    justify-content: center;
  }
  .label {
    width: 537px;
    height: 780px;
    display: block;
  }
  .label-sheet { fill: var(--label-white); stroke: var(--ink); stroke-width: 5; }
  .brand-ribbon, .name-band { fill: var(--leaf-green); }
  .seal-gap { fill: var(--label-white); }
  .seal-ring { fill: var(--label-white); stroke: var(--ink); stroke-width: 3; }
  .divider { stroke: var(--ink); stroke-width: 4; }
  .brand-name {
    font-family: 'Roboto Slab', serif;
    font-weight: 500;
    font-size: 30px;
    fill: var(--brand-plum);
  }
  .product-name {
    font-family: 'Bebas Neue', sans-serif;
    font-size: 112px;
    fill: var(--label-white);
    letter-spacing: 3px;
  }
  .lead-copy {
    font-family: 'Roboto Slab', serif;
    font-weight: 500;
    font-size: 15.5px;
    fill: var(--ink);
  }
  .fine-copy {
    font-family: 'Roboto Slab', serif;
    font-weight: 400;
    font-size: 11.5px;
    fill: var(--ink);
  }
  .contact-text {
    font-family: 'Roboto Slab', serif;
    font-weight: 400;
    font-size: 16px;
    fill: var(--ink);
  }
  .contact-badge { fill: var(--leaf-green); }
  .contact-glyph { fill: var(--label-white); }
  .contact-glyph-line { fill: none; stroke: var(--label-white); stroke-width: 1.4; }
</style>
</head>
<body>
<main class="canvas">
  <svg class="label" viewBox="0 0 687 997" role="img" aria-label="Tallow Creek Farm product label">
    <rect class="label-sheet" x="2.5" y="2.5" width="682" height="992"/>

    <!-- brand seal -->
    <rect class="brand-ribbon" x="168" y="5" width="350" height="165"/>
    <circle class="seal-gap" cx="343" cy="284" r="208"/>
    <circle class="seal-ring" cx="343" cy="284" r="196"/>
    <text class="brand-name" x="343" y="362" text-anchor="middle" textLength="290" lengthAdjust="spacingAndGlyphs">TALLOW CREEK FARM</text>

    <!-- product name band -->
    <line class="divider" x1="5" y1="577" x2="682" y2="577"/>
    <polygon class="name-band"
      points="43,512 645,512 645,699 637,687 629,699 621,687 613,699 605,687 597,699 589,687 581,699 573,687 565,699 557,687 549,699 541,687 533,699 525,687 517,699 509,687 501,699 493,687 485,699 477,687 469,699 461,687 453,699 445,687 437,699 429,687 421,699 413,687 405,699 397,687 389,699 381,687 373,699 365,687 357,699 349,687 341,699 333,687 325,699 317,687 309,699 301,687 293,699 285,687 277,699 269,687 261,699 253,687 245,699 237,687 229,699 221,687 213,699 205,687 197,699 189,687 181,699 173,687 165,699 157,687 149,699 141,687 133,699 125,687 117,699 109,687 101,699 93,687 85,699 77,687 69,699 61,687 53,699 43,687"/>
    <text class="product-name" x="343" y="638" text-anchor="middle" textLength="525" lengthAdjust="spacingAndGlyphs">PRODUCT NAME</text>

    <!-- description -->
    <text class="lead-copy" x="343" y="734" text-anchor="middle" textLength="482" lengthAdjust="spacingAndGlyphs">LOREM IPSUM DOLOR SIT AMET, CONSECTETUR ADIPISCING</text>
    <text class="lead-copy" x="343" y="755" text-anchor="middle" textLength="356" lengthAdjust="spacingAndGlyphs">ELIT, SED DO EIUSMOD TEMPOR INCIDIDUNT</text>
    <text class="fine-copy" x="343" y="784" text-anchor="middle" textLength="288" lengthAdjust="spacingAndGlyphs">LOREM IPSUM DOLOR SIT AMET, CONSECTETUR</text>
    <text class="fine-copy" x="343" y="798" text-anchor="middle" textLength="208" lengthAdjust="spacingAndGlyphs">ADIPISCING ELIT, SED DO EIUSMOD</text>
    <text class="fine-copy" x="343" y="812" text-anchor="middle" textLength="124" lengthAdjust="spacingAndGlyphs">TEMPOR INCIDIDUNT</text>

    <!-- contact row -->
    <g class="contact phone">
      <circle class="contact-badge" cx="36" cy="845" r="11"/>
      <path class="contact-glyph" d="M31 839 q1-2 3-1 l2 3 q0 1-1 2 q1 3 4 4 q1-1 2-1 l3 2 q1 2-1 3 q-3 2-8-2 q-5-5-4-10z"/>
      <text class="contact-text" x="56" y="851" textLength="98" lengthAdjust="spacingAndGlyphs">08 5550 1420</text>
    </g>
    <g class="contact address">
      <circle class="contact-badge" cx="186" cy="845" r="11"/>
      <path class="contact-glyph" d="M186 853 l-5-7 a6 6 0 1 1 10 0z"/>
      <circle class="contact-badge" cx="186" cy="842" r="2"/>
      <text class="contact-text" x="206" y="851" textLength="240" lengthAdjust="spacingAndGlyphs">ROAD NAME, COUNTRY, 23459</text>
    </g>
    <g class="contact web">
      <circle class="contact-badge" cx="473" cy="845" r="11"/>
      <circle class="contact-glyph-line" cx="473" cy="845" r="6"/>
      <ellipse class="contact-glyph-line" cx="473" cy="845" rx="2.5" ry="6"/>
      <line class="contact-glyph-line" x1="467" y1="845" x2="479" y2="845"/>
      <text class="contact-text" x="493" y="851" textLength="168" lengthAdjust="spacingAndGlyphs">WWW.WEBSITE.COM</text>
    </g>
  </svg>
</main>
</body>
</html>
```